Business Card - connecting 2 souls and beggining the journey of self discovery

Logo on the front
with tag line

On the back list of services and contact details

Seminars
workshops
Coaching
podcasts

Daniel Porthwick
Health & Wellbeing Life Coach
0491 372 815
daniel@wovenpathwellness.example
wovenpathwellness.example

Industry/Entity Type

Life Coaching

Contact Information for Business Card

I like the use of colour from the logo to be used. I'm not a fan of white.

Requirements
Must have
• My tagline: The journey home starts with you
Nice to have
• Use of colour that is in the mind body soul logo

```html
<!DOCTYPE html>
<html lang="en">
<head>
<meta charset="utf-8">
<title>Woven Path Wellness – Business Card</title>
<link href="https://fonts.googleapis.com/css2?family=Montserrat:wght@400&family=Source+Sans+3:wght@400;600;700&display=swap" rel="stylesheet">
<style>
  :root {
    --backdrop: #cfcfcf;
    --card-grey: #808385;
    --card-white: #ffffff;
    --ink-grey: #7d7f81;
    --ink-purple: #7b4a9b;
    --accent-orange: #f5a623;
    --divider-gold: #c9b98a;
    --mark-fill: #9a5aa8;
    --accent-soft-a: #b58cc4;
    --accent-soft-b: #f2c07a;
    --text-white: #ffffff;
  }
  * { margin: 0; padding: 0; box-sizing: border-box; }
  html, body {
    width: 1200px; height: 947px; overflow: hidden;
    background: var(--backdrop);
    font-family: "Source Sans 3", "Helvetica Neue", Arial, sans-serif;
  }
  .stage { position: relative; width: 1200px; height: 947px; }
  .card {
    position: absolute; left: 263px; width: 674px; height: 386px;
    box-shadow: 2px 3px 6px rgba(0,0,0,0.25);
    overflow: hidden;
  }
  .card--front { top: 81px; background: var(--card-grey); }
  .card--back { top: 482px; background: var(--card-white); }

  .brand-dot {
    position: absolute; border-radius: 50%; background: var(--mark-fill);
    left: 50%; transform: translateX(-50%);
  }
  .card--front .brand-dot { top: 98px; width: 128px; height: 128px; }
  .card--back .brand-dot { top: 36px; width: 88px; height: 88px; }

  .brand-name {
    position: absolute; left: 0; width: 100%; text-align: center;
    font-family: "Montserrat", "Helvetica Neue", Arial, sans-serif;
    font-weight: 400; letter-spacing: -0.5px;
  }
  .card--front .brand-name { top: 242px; font-size: 31px; color: var(--text-white); }
  .card--back .brand-name { top: 144px; font-size: 22px; color: var(--ink-grey); }

  .tagline {
    position: absolute; top: 335px; left: 0; width: 100%; text-align: center;
    font-size: 17px; color: var(--text-white);
  }

  .person { position: absolute; right: 380px; top: 230px; text-align: right; }
  .person__name { font-size: 28px; font-weight: 700; color: var(--ink-purple); line-height: 1.05; }
  .person__role { font-size: 17px; color: var(--ink-grey); line-height: 1.3; }

  .divider {
    position: absolute; left: 314px; top: 219px; width: 1.5px; height: 61px;
    background: var(--divider-gold);
  }

  .contact { position: absolute; left: 340px; top: 216px; list-style: none; }
  .contact li {
    display: flex; align-items: center; height: 22px;
    font-size: 17px; font-weight: 600; color: var(--ink-grey);
  }
  .contact svg { width: 15px; height: 15px; margin-right: 7px; flex: none; }

  .accent-strip {
    position: absolute; left: 0; bottom: 34px; width: 100%; height: 4px;
    background: linear-gradient(90deg, var(--accent-soft-a), var(--accent-soft-b));
  }
  .services-band {
    position: absolute; left: 0; bottom: 0; width: 100%; height: 32px;
    background: var(--card-grey);
    display: flex; align-items: center; justify-content: center;
    font-size: 17px; color: var(--text-white);
  }
  .services-band span + span::before { content: "•"; margin: 0 8px; font-size: 12px; vertical-align: 2px; }
</style>
</head>
<body>
<main class="stage">

  <section class="card card--front" aria-label="Card front">
    <div class="brand-dot"></div>
    <p class="brand-name">Woven Path Wellness</p>
    <p class="tagline">The journey home starts with you</p>
  </section>

  <section class="card card--back" aria-label="Card back">
    <div class="brand-dot"></div>
    <p class="brand-name">Woven Path Wellness</p>

    <div class="person">
      <p class="person__name">Daniel Porthwick</p>
      <p class="person__role">Life Coach</p>
    </div>
    <div class="divider"></div>

    <ul class="contact">
      <li>
        <svg viewBox="0 0 16 16"><path d="M3.5 1.5l2.5 0 1 3.5-1.7 1.2a9 9 0 0 0 4.5 4.5L11 9l3.5 1v2.5c0 1-1 2-2 2C6.5 14.5 1.5 9.5 1.5 3.5c0-1 1-2 2-2z" fill="var(--accent-orange)"/></svg>
        0491 372 815
      </li>
      <li>
        <svg viewBox="0 0 16 16"><rect x="1.5" y="3.5" width="13" height="9" fill="none" stroke="var(--accent-orange)" stroke-width="1.5"/><path d="M1.5 3.5l6.5 5 6.5-5" fill="none" stroke="var(--accent-orange)" stroke-width="1.5"/></svg>
        daniel@wovenpathwellness.example
      </li>
      <li>
        <svg viewBox="0 0 16 16" fill="none" stroke="var(--accent-orange)" stroke-width="1.3"><circle cx="8" cy="8" r="6.5"/><ellipse cx="8" cy="8" rx="2.8" ry="6.5"/><path d="M1.5 8h13M2.5 4.8h11M2.5 11.2h11"/></svg>
        wovenpathwellness.example
      </li>
    </ul>

    <div class="accent-strip" role="img" aria-label="Decorative colour accent above the services band"></div>
    <p class="services-band"><span>Seminars</span><span>Workshops</span><span>Coaching</span><span>Podcasts</span></p>
  </section>

</main>
</body>
</html>
```